Graduation Day Sale Banner Ad for Website

We need a banner for our upscale jewelry website. Banner must have a classy high end look. The size of the banner must be 1187 × 400. I have attached pieces we would like used (some or all). The banner is for a Graduation Day sale that we are running. The banner should say "Graduation Day Gifts on Sale"

Target Market(s)

Wealthy individuals looking to buy graduation gifts for their children

Industry/Entity Type

Jewelry

Requirements
Must have
• Must match the look and feel of the website (www.velmira-studio.com)

```html
<!DOCTYPE html>
<html lang="en">
<head>
<meta charset="utf-8">
<title>Graduation Day Gifts on Sale</title>
<link rel="stylesheet" href="https://fonts.googleapis.com/css2?family=Raleway:wght@400;700;800&display=swap">
<style>
  :root {
    --bg-light: #fdf9f6;
    --bg-peach: #f1d9c7;
    --bg-warm: #e9c6ad;
    --ribbon-red: #e8322c;
    --ribbon-glow: #f4604f;
    --ribbon-deep: #d8221f;
    --text-white: #ffffff;
    --gold-light: #f0d28a;
    --gold: #dcae4c;
    --silver-light: #f1f1f3;
    --silver: #d6d6db;
  }
  * { margin: 0; padding: 0; box-sizing: border-box; }
  html, body { width: 1200px; height: 404px; overflow: hidden; }
  body { font-family: "Raleway", sans-serif; background: var(--bg-light); }

  .banner {
    position: relative;
    width: 1200px;
    height: 404px;
    overflow: hidden;
    background:
      radial-gradient(ellipse 520px 260px at 300px 210px, var(--bg-light) 0%, rgba(253,249,246,0) 70%),
      radial-gradient(ellipse 400px 300px at 1120px 200px, #fbf2ec 0%, rgba(251,242,236,0) 70%),
      linear-gradient(160deg, var(--bg-peach) 0%, #f7e8de 40%, var(--bg-warm) 100%);
  }

  .product-photo {
    position: absolute;
    border-radius: 14px;
  }

  .product-rings {
    left: 106px;
    top: 156px;
    width: 256px;
    height: 240px;
    background: linear-gradient(135deg, var(--gold-light) 0%, var(--gold) 55%, var(--silver) 100%);
  }

  .product-pendant {
    left: 426px;
    top: 0;
    width: 156px;
    height: 226px;
    border-radius: 0 0 14px 14px;
    background: linear-gradient(180deg, var(--silver-light) 0%, var(--silver) 100%);
  }

  .ribbon {
    position: absolute;
    left: 700px;
    top: 0;
    width: 332px;
    height: 394px;
  }

  .ribbon-text {
    position: absolute;
    left: 700px;
    top: 0;
    width: 332px;
    text-align: center;
    color: var(--text-white);
  }

  .headline {
    margin-top: 38px;
    font-weight: 700;
    font-size: 40px;
    line-height: 42px;
    letter-spacing: 0.3px;
  }

  .subline {
    display: flex;
    align-items: center;
    justify-content: center;
    gap: 12px;
    margin-top: 25px;
    font-weight: 400;
    font-size: 18px;
    line-height: 22px;
    letter-spacing: 0.5px;
  }
  .subline::before,
  .subline::after {
    content: "";
    width: 58px;
    height: 2px;
    background: var(--text-white);
  }

  .sale-word {
    margin-top: 12px;
    font-weight: 800;
    font-size: 64px;
    line-height: 68px;
    letter-spacing: 1px;
  }
</style>
</head>
<body>
  <main class="banner">
    <div class="product-photo product-rings" role="img" aria-label="Gold pearl ring with diamonds beside a gold and steel band ring"></div>
    <div class="product-photo product-pendant" role="img" aria-label="Diamond pavé heart pendant with sapphires on a white gold chain"></div>

    <svg class="ribbon" viewBox="0 0 332 394" aria-hidden="true">
      <defs>
        <radialGradient id="ribbonFill" cx="50%" cy="40%" r="70%">
          <stop offset="0%" stop-color="#f4604f"/>
          <stop offset="60%" stop-color="#e8322c"/>
          <stop offset="100%" stop-color="#d8221f"/>
        </radialGradient>
      </defs>
      <path d="M0 0 H332 V394 L166 270 L0 394 Z" fill="url(#ribbonFill)"/>
      <path d="M10 0 V370 L166 254 L322 370 V0" fill="none" stroke="#ffffff" stroke-width="1.5" stroke-dasharray="5 4"/>
    </svg>

    <div class="ribbon-text">
      <h1 class="headline">GRADUATION<br>DAY</h1>
      <p class="subline">GIFTS ON</p>
      <p class="sale-word">SALE</p>
    </div>
  </main>
</body>
</html>
```